Law Offices business card

Hi there, I'll need business card for the Law Offices of Tobin Haskell. The information must convey his strategic approach and quick resolution to complex business litigation needs. Please emphasize Civil Litigation, Corporate Law, Business Governance and Real Estate Law. Tobin has over 25 years of experience in these fields.The card should be modern and edgy and the message should be clear. Please consult his current website for ideas.

Business

```html
<!DOCTYPE html>
<html lang="en">
<head>
<meta charset="UTF-8">
<title>Law Offices of Tobin Haskell – Business Card</title>
<link rel="stylesheet" href="https://fonts.googleapis.com/css2?family=Open+Sans:wght@400;600;700&display=swap">
<style>
  :root {
    --backdrop: #2b2b2d;
    --card-white: #ffffff;
    --card-dark: #232323;
    --ink: #2a2a2a;
    --accent-red: #e0262b;
    --lavender: #c9c7dc;
    --muted-light: #d6d5e2;
    --divider: #5a5a5e;
  }
  * { box-sizing: border-box; margin: 0; padding: 0; }
  html, body {
    width: 1200px; height: 900px; overflow: hidden;
    background: var(--backdrop);
    font-family: "Open Sans", Arial, sans-serif;
  }
  .canvas { position: relative; width: 1200px; height: 900px; }
  .card {
    position: absolute; width: 560px; height: 320px;
    border-radius: 18px; box-shadow: 0 14px 30px rgba(0,0,0,.45);
  }
  .card--front { left: 60px; top: 110px; background: var(--card-white); }
  .card--back { left: 580px; top: 470px; background: var(--card-dark); }

  .firm-name {
    position: absolute; display: flex; align-items: center; gap: 12px;
  }
  .firm-name__mark { width: 14px; height: 14px; background: var(--accent-red); flex: none; }
  .firm-name__text { font-weight: 700; line-height: 1.05; white-space: nowrap; }
  .firm-name__small { display: block; font-size: 17px; letter-spacing: 2px; }
  .firm-name__large { display: block; font-size: 44px; letter-spacing: -0.5px; }

  .card--front .firm-name { left: 100px; top: 78px; color: var(--ink); }
  .services {
    position: absolute; left: 250px; top: 200px;
    font-size: 13px; line-height: 1.5; color: var(--ink); letter-spacing: .4px;
  }
  .services__highlight { color: var(--accent-red); }

  .card--back .firm-name { left: 30px; top: 150px; color: var(--lavender); }
  .card--back .firm-name__small { font-size: 12px; }
  .card--back .firm-name__large { font-size: 28px; }
  .card-divider { position: absolute; left: 318px; top: 40px; }

  .contact { position: absolute; left: 362px; top: 48px; color: var(--muted-light); }
  .contact__name { font-weight: 700; font-size: 18px; color: var(--lavender); letter-spacing: .3px; white-space: nowrap; }
  .contact__title { font-weight: 600; font-size: 11px; color: var(--accent-red); letter-spacing: .8px; margin-bottom: 8px; }
  .contact__address { font-size: 13px; line-height: 1.4; margin-bottom: 12px; padding-left: 20px; }
  .contact__list { list-style: none; font-size: 13px; line-height: 1.55; }
  .contact__item { display: flex; align-items: center; gap: 8px; white-space: nowrap; }
  .contact__icon { width: 12px; height: 12px; fill: var(--accent-red); flex: none; }
</style>
</head>
<body>
<main class="canvas">

  <section class="card card--front" aria-label="Card front">
    <div class="firm-name">
      <span class="firm-name__mark"></span>
      <span class="firm-name__text">
        <span class="firm-name__small">LAW OFFICES OF</span>
        <span class="firm-name__large">Tobin Haskell, PA</span>
      </span>
    </div>
    <p class="services">
      BUSINESS LITIGATION<br>
      <span class="services__highlight">REAL ESTATE</span><br>
      TITLE AND CLOSING SERVICES
    </p>
  </section>

  <section class="card card--back" aria-label="Card back">
    <div class="firm-name">
      <span class="firm-name__mark"></span>
      <span class="firm-name__text">
        <span class="firm-name__small">LAW OFFICES OF</span>
        <span class="firm-name__large">Tobin Haskell, PA</span>
      </span>
    </div>

    <svg class="card-divider" width="30" height="240" viewBox="0 0 30 240" aria-hidden="true">
      <line x1="2" y1="0" x2="28" y2="240" stroke="var(--divider)" stroke-width="1.5"/>
    </svg>

    <div class="contact">
      <p class="contact__name">TOBIN HASKELL</p>
      <p class="contact__title">ATTORNEY</p>
      <p class="contact__address">318B Harbor Street<br>Coral Bay, FL 33999</p>
      <ul class="contact__list">
        <li class="contact__item">
          <svg class="contact__icon" viewBox="0 0 24 24" aria-hidden="true"><path d="M6.6 10.8a15.1 15.1 0 0 0 6.6 6.6l2.2-2.2a1 1 0 0 1 1-.25 11.4 11.4 0 0 0 3.6.57 1 1 0 0 1 1 1V20a1 1 0 0 1-1 1A17 17 0 0 1 3 4a1 1 0 0 1 1-1h3.5a1 1 0 0 1 1 1c0 1.25.2 2.450.57 3.6a1 1 0 0 1-.25 1z"/></svg>
          555-014-2136
        </li>
        <li class="contact__item">
          <svg class="contact__icon" viewBox="0 0 24 24" aria-hidden="true"><rect x="6" y="1" width="12" height="22" rx="2"/></svg>
          555-018-2367
        </li>
        <li class="contact__item">
          <svg class="contact__icon" viewBox="0 0 24 24" aria-hidden="true"><path d="M2 5h20v14H2z M2 5l10 8 10-8" fill="none" stroke="var(--accent-red)" stroke-width="2.5"/></svg>
          tobin@haskellfirm.com
        </li>
        <li class="contact__item">
          <svg class="contact__icon" viewBox="0 0 24 24" aria-hidden="true"><circle cx="12" cy="12" r="10" fill="none" stroke="var(--accent-red)" stroke-width="2.5"/><path d="M2 12h20M12 2c3 3 3 17 0 20M12 2c-3 3-3 17 0 20" fill="none" stroke="var(--accent-red)" stroke-width="2"/></svg>
          www.haskellfirm.com
        </li>
      </ul>
    </div>
  </section>

</main>
</body>
</html>
```